Business Card for Polygraph business in Africa

Business Card . Polygraph Examiner based in Tanzania, East Africa.
Business Card will be used to disseminate contact information to potential clients.
It should convey that I am a professional specifically in the polygraph field and perform my work with integrity.

I have attached the business card that I'm currently using, which I threw together myself initially. It's not professional enough.

Target Market(s)

Banks, Accounting Firms, Government Ministries, Gas, Oil, & Gemstone Mining Concerns, Wildlife Conservation NGOs, International companies located in East Africa.

Industry/Entity Type

Business

Contact Information for Business Card

Veritas Lumeno
Harriet Munsell
PO Box 48317
Arusha, Tanzania
+255 712 839 254
harrietmunsell@quillpost.example

Colors
00a990
f37122
faa54b

Requirements
Must have
• - Veritas Lumeno (with the word "Polygraph" being more prominent than the word "Tanzania")
• - Forensic Examinations
• - Employment Screening
• - Should contain a logo of the Continental Truthfinder Guild (of which I'm a member)
• - I would like an accent design (such as the polygraph "squiggles" of a cardio tracing or such as that)
• - My contact information (less prominent, but large enough to read legibly). I would also consider putting the contact information on the second side of the card.
Nice to have
• My color suggestions are changeable.
Should not have
• Anything "cutesy" or "cartoonish"

```html
<!DOCTYPE html>
<html lang="en">
<head>
<meta charset="utf-8">
<title>Veritas Lumeno – Business Card</title>
<link rel="stylesheet" href="https://fonts.googleapis.com/css2?family=Open+Sans:wght@400;600&display=swap">
<style>
  :root {
    --teal: #00a990;
    --orange: #f37122;
    --orange-soft: #faa54b;
    --ink: #5a5a5a;
    --ink-strong: #3f3f3f;
    --paper: #ffffff;
    --backdrop: #e9e7e3;
    --badge: #3b3a98;
  }
  * { box-sizing: border-box; margin: 0; padding: 0; }
  html, body { width: 1200px; height: 780px; overflow: hidden; }
  body {
    background: var(--backdrop);
    font-family: "Open Sans", Arial, sans-serif;
    display: flex; align-items: center; justify-content: center; gap: 40px;
  }
  .card {
    position: relative; width: 560px; height: 320px;
    background: var(--paper); overflow: hidden;
    box-shadow: 0 6px 18px rgba(0,0,0,.18);
  }
  .card-art { position: absolute; inset: 0; width: 100%; height: 100%; }
  .wordmark {
    position: absolute; left: 0; right: 0; text-align: center;
    font-weight: 600; color: var(--teal); letter-spacing: .5px; white-space: nowrap;
  }
  .front .wordmark { top: 74px; font-size: 38px; }
  .guild-badge {
    position: absolute; right: 14px; top: 20px; width: 58px; height: 58px;
    border-radius: 50%; background: var(--paper);
    border: 3px solid var(--badge); box-shadow: 0 0 0 2px var(--paper);
  }
  .contact {
    position: absolute; left: 118px; top: 196px;
    color: var(--ink); font-size: 12.5px; line-height: 1.55;
  }
  .contact-name { font-size: 18px; font-weight: 600; color: var(--ink-strong); margin-bottom: 4px; }
  .contact-line { display: flex; align-items: center; gap: 7px; }
  .contact-icon { width: 15px; height: 15px; flex: none; }
  .back .wordmark { top: 96px; font-size: 40px; }
  .back .card-art { background: linear-gradient(160deg, #ffffff 0%, #f1f1f1 100%); }
  .services {
    position: absolute; left: 132px; top: 162px;
    color: var(--ink); font-size: 13.5px; line-height: 1.5;
  }
</style>
</head>
<body>

<section class="card front" aria-label="Card front">
  <svg class="card-art" viewBox="0 0 560 320" aria-hidden="true">
    <rect width="560" height="320" fill="var(--teal)"/>
    <path d="M74,0 Q-6,160 74,320 L486,320 Q566,160 486,0 Z" fill="var(--paper)"/>
    <path d="M80,0 Q2,160 80,320 L480,320 Q558,160 480,0 Z" fill="var(--orange)"/>
    <path d="M90,0 Q14,160 90,320 L470,320 Q546,160 470,0 Z" fill="var(--paper)"/>
  </svg>
  <div class="guild-badge" role="img" aria-label="Continental Truthfinder Guild member badge"></div>
  <div class="wordmark">Veritas Lumeno</div>
  <div class="contact">
    <p class="contact-name">Harriet Munsell</p>
    <p>PO Box 48317</p>
    <p>Arusha, Tanzania</p>
    <p class="contact-line">
      <svg class="contact-icon" viewBox="0 0 16 16" aria-hidden="true">
        <circle cx="8" cy="8" r="7" fill="none" stroke="var(--orange)" stroke-width="1.3"/>
        <rect x="5.5" y="3.8" width="5" height="8.4" rx="1" fill="none" stroke="var(--orange)" stroke-width="1.2"/>
      </svg>+255 712 839 254</p>
    <p class="contact-line">
      <svg class="contact-icon" viewBox="0 0 16 16" aria-hidden="true">
        <circle cx="8" cy="8" r="7" fill="none" stroke="var(--orange)" stroke-width="1.3"/>
        <rect x="4" y="5.3" width="8" height="5.6" fill="none" stroke="var(--orange)" stroke-width="1.2"/>
        <path d="M4,5.3 L8,8.6 L12,5.3" fill="none" stroke="var(--orange)" stroke-width="1.2"/>
      </svg>harrietmunsell@quillpost.example</p>
  </div>
</section>

<section class="card back" aria-label="Card back">
  <svg class="card-art" viewBox="0 0 560 320" aria-hidden="true">
    <path d="M0,196 Q250,300 560,300" fill="none" stroke="var(--orange)" stroke-width="6"/>
    <path d="M0,206 Q250,306 560,310 L560,320 L0,320 Z" fill="var(--teal)"/>
  </svg>
  <div class="wordmark">Veritas Lumeno</div>
  <div class="services">
    <p>Issue Investigation</p>
    <p>Employment Screening</p>
  </div>
</section>

</body>
</html>
```